Solar Energy Technology Company - Solar Savings Analysis Flyer

I Have Included The Text Content I Want Put On An 8 1/2 " x 11" Flyer.

I Want To See It In One Page Format And In Tri-Fold Brochure Format.

It Needs To Grab And Captivate Prospective Customers, Awesome Graphics, Layout, Etc.

We Are A Cutting Edge Solar Energy Solutions & Technology Company.

We Need A World Class High Tech Look and Logo For Our Company Included On Our 8 1/2 x 11 Flyer & Trifold Brochure

Brightfold Venture Partners, LLC
"Forward Ideas Delivered"

Would Like A Black Gold And Electric Blue Color Scheme, However, We We Are Open To Seeing Your Creativity, Colors, Graphics Etc. For Consideration.

Target Market(s)

Homeowners Without Solar Panels On Their Roof

Industry/Entity Type

New Roof Top Solar Energy Producing Panel Technology Systems

Font styles to use
Serif

Requirements
Must have
• See My Attached Flyer/Trifold Brochure Display Content
Nice to have
• Gold Black And Electric Blue Color Scheme, Solar Theme Background Graphics

```html
<!DOCTYPE html>
<html lang="en">
<head>
<meta charset="utf-8">
<title>Solar Savings Analysis Flyer</title>
<link href="https://fonts.googleapis.com/css2?family=Bitter:wght@400;600;700;800&display=swap" rel="stylesheet">
<style>
:root{
  --blue:#4a5fb5;
  --gold:#e3920a;
  --ink:#111111;
  --paper:#ffffff;
  --stage:#e6e7e8;
  --tag:#c9cde8;
}
*{margin:0;padding:0;box-sizing:border-box}
html,body{width:1200px;height:1200px;overflow:hidden;background:var(--stage)}
body{position:relative;font-family:'Bitter',Georgia,serif;color:var(--ink)}
.flyer{
  position:absolute;left:167px;top:40px;width:1160px;height:1500px;
  background:var(--paper);transform:scale(0.7467);transform-origin:0 0;
  overflow:hidden;box-shadow:12px 12px 24px rgba(0,0,0,.35);
}
.art{position:absolute;inset:0;width:1160px;height:1500px}
.r{position:absolute;right:44px;text-align:right;white-space:nowrap}
.headline{top:32px;font-size:76px;font-weight:800;color:var(--blue);letter-spacing:0.5px}
.question{top:114px;font-size:32px;font-weight:400}
.offer{top:150px;font-size:74px;font-weight:800;color:var(--gold)}
.condition{top:238px;font-size:23px;font-weight:800}
.reduction{top:265px;font-size:33px;font-weight:800}
.reduction span{color:var(--gold);text-decoration:underline;text-decoration-thickness:3px;text-underline-offset:4px}
.summary{top:316px;font-size:17px;line-height:21px}
.payment-bar{
  position:absolute;left:269px;top:387px;width:846px;height:40px;background:var(--gold);
  border-radius:4px;font-size:24px;font-weight:700;line-height:40px;text-align:center;white-space:nowrap;
}
.tier{position:absolute;width:205px;height:167px;border-radius:6px;overflow:hidden;background:var(--paper);text-align:center;box-shadow:0 2px 3px rgba(0,0,0,.2)}
.tier-head{background:var(--gold);height:44px;font-size:28px;font-weight:800;line-height:48px}
.tier-label{height:52px;font-size:16px;font-weight:700;line-height:21px;padding-top:5px}
.tier-price{background:var(--gold);height:40px;font-size:28px;font-weight:800;line-height:40px}
.tier-save{background:var(--ink);color:var(--paper);height:25px;font-size:16px;line-height:24px;white-space:nowrap}
.tier-foot{background:var(--gold);height:6px}
.gift{position:absolute;left:802px;top:818px;width:312px;font-size:17px;line-height:20.6px}
.gift em{font-style:normal;font-weight:700;color:var(--gold)}
.website{position:absolute;left:897px;top:1080px;font-size:15.5px;line-height:19px;white-space:nowrap}
.website b{color:var(--gold)}
.brand{position:absolute;left:742px;top:1262px;display:flex;align-items:center;gap:16px}
.brand-dot{width:50px;height:50px;border-radius:50%;background:var(--gold);flex:none}
.brand-name{font-size:26px;line-height:30px;font-weight:600;color:var(--gold);white-space:nowrap}
.brand-tag{position:absolute;left:808px;top:1332px;font-size:16px;color:var(--tag);white-space:nowrap}
.contact{position:absolute;left:692px;color:var(--paper);white-space:nowrap}
.contact-phone{top:1376px;font-size:26px}
.contact-phone b{font-weight:800}
.contact-line{font-size:15.5px}
.contact-line b{font-weight:800}
.corp{top:1436px}
.regional{top:1468px}
</style>
</head>
<body>
<main class="flyer">
  <svg class="art" viewBox="0 0 1160 1500">
    <defs>
      <linearGradient id="nightSky" x1="0" y1="0" x2="0.4" y2="1">
        <stop offset="0" stop-color="#2f3f9a"/>
        <stop offset="0.55" stop-color="#2a2560"/>
        <stop offset="1" stop-color="#3a63a8"/>
      </linearGradient>
    </defs>
    <polygon role="img" aria-label="Illustration of a house at night with solar panels on its roof and lit windows"
      fill="url(#nightSky)" points="0,175 515,840 655,725 905,1225 750,1225 535,1500 0,1500"/>
    <polygon class="bolt" fill="var(--gold)" points="0,165 515,832 655,720 912,1225 850,1225 655,790 382,945 0,200"/>
    <polygon class="footer-panel" fill="var(--ink)" points="755,1225 1160,1225 1160,1500 538,1500"/>
    <polyline fill="none" stroke="var(--gold)" stroke-width="6" points="530,1500 750,1220 1160,1220"/>
  </svg>

  <h1 class="r headline">ATTENTION HOMEOWNER!</h1>
  <p class="r question">Are You FED UP With Your HIGH Electric Bills?</p>
  <p class="r offer">We Will Pay You $2,000…</p>
  <p class="r condition">…WHEN YOU ALLOW US TO PERMANENTLY LOWER</p>
  <p class="r reduction">YOUR ELECTRIC BILL By <span>At Least 25% To 50%!</span></p>
  <p class="r summary">On Average, We SAVE Homeowners *33% OFF Their Electricity Cost Every Month With Our<br>NEW Cutting Edge ADVANCED SOLAR TECHNOLOGY, WITHOUT TAKING 1 PENNY FROM<br>YOUR CURRENT MONTHLY BUDGET. GOVERNMENT SUBSIDIZED!</p>

  <div class="payment-bar">*IF YOUR Last 12 Months “Average Monthly Electric Payment” Is…</div>

  <section class="tier" style="left:472px;top:440px">
    <div class="tier-head">*$100:</div><div class="tier-label">Your NEW Monthly<br>Fixed Payment Will Be</div>
    <div class="tier-price">$67</div><div class="tier-save">($396 Annual Savings)</div><div class="tier-foot"></div>
  </section>
  <section class="tier" style="left:691px;top:440px">
    <div class="tier-head">*$200:</div><div class="tier-label">Your NEW Monthly<br>Fixed Payment Will Be</div>
    <div class="tier-price">$134</div><div class="tier-save">($792 Annual Savings)</div><div class="tier-foot"></div>
  </section>
  <section class="tier" style="left:909px;top:440px">
    <div class="tier-head">*$300:</div><div class="tier-label">Your NEW Monthly<br>Fixed Payment Will Be</div>
    <div class="tier-price">$201</div><div class="tier-save">($1,188 Annual Savings)</div><div class="tier-foot"></div>
  </section>
  <section class="tier" style="left:691px;top:622px">
    <div class="tier-head">*$400:</div><div class="tier-label">Your NEW Monthly<br>Fixed Payment Will Be</div>
    <div class="tier-price">$268</div><div class="tier-save">($1,584 Annual Savings)</div><div class="tier-foot"></div>
  </section>
  <section class="tier" style="left:909px;top:622px">
    <div class="tier-head">*$500:</div><div class="tier-label">Your NEW Monthly<br>Fixed Payment Will Be</div>
    <div class="tier-price">$335</div><div class="tier-save">($1,980 Annual Savings)</div><div class="tier-foot"></div>
  </section>

  <p class="gift">If you own your home, we will send you our “<em>NOBEL PRIZE WINNING TECHNOLOGY</em>” THAT WILL ELIMINATE $200 OF YOUR GAS OR DIESEL FUEL EXPENSE When you allow us to do a no cost, no obligation energy savings analysis and share your money saving results with you via a 30 minute zoom meeting.</p>

  <p class="website">Visit Our Website @<br><b>www.SunwardSavings.energy</b><br>To Request Your Complimentary<br>Energy Savings Analysis<br>And To Accept Our $200 Gift.</p>

  <div class="brand"><span class="brand-dot"></span><span class="brand-name">Brightfold Venture<br>Partners, LLC</span></div>
  <p class="brand-tag">“Forward Ideas Delivered”</p>

  <p class="contact contact-phone"><b>888-555-0142</b> Ext. 204 Dana Morrow</p>
  <p class="contact contact-line corp"><b>CORP OFFICE:</b> 4120 Canyon Ridge Dr. Henderson, NV 89052</p>
  <p class="contact contact-line regional"><b>REGIONAL OFFICE:</b> 1785 Orchard View Rd. Fresno, CA 93720</p>
</main>
</body>
</html>
```